Professional banners for an eyewear company

I have 3 images which need to be made into banners. Size 990 x 370, with a 10 pixel white border at top and bottom of banner.

They all need to be adjusted to make the colours better and less bright.
All will need some writing written on them with a nice serif font.

Banner 1 text: Handcrafted luxury eyewear, with a purpose...
Banner 2 text: Half of our profits go to help malnourished children in India
Banner 3 text: 10% of your first order, use code: First Order

On our homepage these 3 banners will alternate, so they need to look good together.

Tips
Please take a look at the banners on the lunvoreck.com homepage, this is kind of how I want the text to be displayed, and they use good colours.

The backgrounds on Banners 2 & 3 can be changed.
Banner 3 background if you can change to a nice colour, as per lunvoreck.com homepage.
Updates

Hi, just a quick update, thank you for all the designs submitted so far, please keep in mind that the brand is a luxury high-end brand so designs will need to reflect this.

Industry/Entity Type

Eyewear

```html
<!DOCTYPE html>
<html lang="en">
<head>
<meta charset="utf-8">
<title>First Order Offer Banner</title>
<link rel="stylesheet" href="https://fonts.googleapis.com/css2?family=Italiana&family=Macondo&display=swap">
<style>
  :root {
    --paper: #ffffff;
    --rose: #e0566a;
    --ink-light: #ffffff;
    --hair: #b8663f;
    --shirt: #f1ece6;
    --skin: #efc2ab;
  }
  html, body {
    margin: 0;
    padding: 0;
    width: 1200px;
    height: 448px;
    overflow: hidden;
    background: var(--paper);
  }
  .banner {
    position: relative;
    width: 1200px;
    height: 448px;
    background: var(--paper);
  }
  .banner__band {
    position: absolute;
    left: 0;
    top: 12px;
    width: 1200px;
    height: 422px;
    background: var(--rose);
  }
  .banner__model {
    position: absolute;
    left: 18px;
    top: 12px;
    width: 310px;
    height: 422px;
    border-radius: 120px 120px 0 0;
    background: linear-gradient(180deg, var(--hair) 0%, var(--skin) 32%, var(--shirt) 55%, var(--shirt) 100%);
  }
  .offer {
    position: absolute;
    color: var(--ink-light);
    margin: 0;
  }
  .offer__amount {
    left: 568px;
    top: -12px;
    font-family: "Italiana", "Didot", serif;
    font-size: 290px;
    line-height: 1;
    font-weight: 400;
    letter-spacing: -6px;
  }
  .offer__percent {
    left: 800px;
    top: 30px;
    font-family: "Italiana", "Didot", serif;
    font-size: 150px;
    line-height: 1;
  }
  .offer__off {
    left: 812px;
    top: 176px;
    font-family: "Italiana", "Didot", serif;
    font-size: 58px;
    line-height: 1;
    letter-spacing: 1px;
  }
  .offer__details {
    left: 330px;
    top: 270px;
    width: 860px;
    text-align: center;
    font-family: "Macondo", "Georgia", serif;
    font-size: 70px;
    line-height: 72px;
    font-weight: 400;
  }
</style>
</head>
<body>
  <div class="banner">
    <div class="banner__band"></div>
    <div class="banner__model" role="img" aria-label="Photo of a red-haired woman in sunglasses and a white polka-dot blouse, touching her hair in surprise"></div>
    <p class="offer offer__amount">10</p>
    <p class="offer offer__percent">%</p>
    <p class="offer offer__off">OFF</p>
    <p class="offer offer__details">your first order,<br>use code: First Order</p>
  </div>
</body>
</html>
```